Email Banner (BrindleNotes)

We require an email banner for our email promotions sent to prospect clients. The banner needs to contain the wording BrindleNotes and use the same colour scheme as the logos attached.

This is for B2B professional's so needs to look like a place you would come to read technology articles.

```html
<!DOCTYPE html>
<html lang="en">
<head>
<meta charset="utf-8">
<title>BrindleNotes Email Banner</title>
<link rel="stylesheet" href="https://fonts.googleapis.com/css2?family=Poppins:wght@600&display=swap">
<style>
  :root {
    --stage: #333333;
    --banner-bg: #ffffff;
    --navy: #22365a;
    --red: #d12b34;
    --pink-soft: #ffadbb;
    --grey-soft: #e1dcdd;
  }
  * { margin: 0; padding: 0; box-sizing: border-box; }
  html, body {
    width: 1200px;
    height: 450px;
    overflow: hidden;
    background: var(--stage);
  }
  .stage {
    width: 1200px;
    height: 450px;
    display: flex;
    align-items: center;
    justify-content: center;
  }
  .email-banner {
    position: relative;
    width: 1200px;
    height: 277px;
    background: var(--banner-bg);
    overflow: hidden;
  }
  .backdrop-art {
    position: absolute;
    inset: 0;
    width: 100%;
    height: 100%;
  }
  .brand {
    position: absolute;
    inset: 0;
    display: flex;
    align-items: center;
    justify-content: center;
    gap: 26px;
  }
  .brand-mark {
    width: 44px;
    height: 44px;
    background: var(--red);
    border-radius: 6px;
  }
  .brand-name {
    font-family: "Poppins", sans-serif;
    font-weight: 600;
    font-size: 112px;
    line-height: 1;
    letter-spacing: -1px;
    color: var(--navy);
  }
</style>
</head>
<body>
  <div class="stage">
    <section class="email-banner">
      <svg class="backdrop-art" viewBox="0 0 1200 277" preserveAspectRatio="none" role="img" aria-label="Soft diagonal pattern of rounded pink and grey strokes behind the name">
        <defs>
          <linearGradient id="backdrop-wash" x1="0" y1="1" x2="1" y2="0">
            <stop offset="0" stop-color="#ffffff" stop-opacity="0"/>
            <stop offset="0.25" stop-color="#e1dcdd" stop-opacity="0.7"/>
            <stop offset="0.5" stop-color="#ffadbb" stop-opacity="0.8"/>
            <stop offset="0.75" stop-color="#ffadbb" stop-opacity="0.6"/>
            <stop offset="1" stop-color="#e1dcdd" stop-opacity="0.7"/>
          </linearGradient>
        </defs>
        <polygon points="120,277 420,0 1200,0 1200,277" fill="url(#backdrop-wash)"/>
      </svg>
      <div class="brand">
        <span class="brand-mark" aria-hidden="true"></span>
        <h1 class="brand-name">BrindleNotes</h1>
      </div>
    </section>
  </div>
</body>
</html>
```